Looking for attractive banner design (print banner)

I am looking to redesign a banner to be more attractive and professional. This will be a print banner, 24" x 36" vertical. I am attaching the original concept to reference. High resolution file for print required. fading or blurring the background, attractive fonts, gradient highlight for text boxes, etc.

```html
<!DOCTYPE html>
<html lang="en">
<head>
<meta charset="utf-8">
<title>Essential Oils for The Horse &amp; Rider</title>
<link rel="stylesheet" href="https://fonts.googleapis.com/css2?family=Anton&family=Norican&family=Outfit:wght@400&family=Pathway+Gothic+One&display=swap">
<style>
  :root{
    --surround:#000;
    --ink:#3b2320;
    --box:rgba(255,255,255,.72);
    --band:rgba(255,245,228,.7);
    --leaf-1:#c89b4c;
    --leaf-2:#a57834;
    --mid:#9c7a4e;
    --sand:#e6ded2;
    --sand-2:#cfc6b8;
  }
  *{box-sizing:border-box;margin:0;padding:0}
  html,body{width:837px;height:1200px;overflow:hidden;background:var(--surround)}
  .poster{position:absolute;left:72px;top:79px;width:694px;height:1040px;overflow:hidden}
  .poster-photo{position:absolute;inset:0;
    background:linear-gradient(180deg,var(--leaf-1) 0%,var(--leaf-2) 30%,var(--mid) 55%,var(--sand-2) 75%,var(--sand) 100%)}
  .title-band{position:absolute;left:0;top:15px;width:694px;height:115px;background:var(--band);text-align:center;color:var(--ink)}
  .title-script{font-family:"Norican",cursive;font-weight:400;font-size:58px;line-height:1;padding-top:14px}
  .title-sub{font-family:"Outfit",sans-serif;font-size:23px;margin-top:2px}
  .topic{position:absolute;background:var(--box);color:var(--ink);padding:4px 0 0 34px}
  .topic.left{left:0;width:208px}
  .topic.right{left:497px;width:197px;text-align:right;padding:4px 25px 0 0}
  .topic h2{font-family:"Anton",sans-serif;font-weight:400;font-size:21px;line-height:26px;letter-spacing:-.3px;white-space:nowrap}
  .topic p{font-family:"Pathway Gothic One",sans-serif;font-size:16px;line-height:19.3px;white-space:nowrap}
  .disclaimer{position:absolute;left:0;top:997px;width:694px;height:26px;background:var(--box);color:var(--ink);
    font-family:"Outfit",sans-serif;font-size:11.5px;line-height:26px;text-align:center;text-transform:uppercase}
</style>
</head>
<body>
<main class="poster">
  <div class="poster-photo" role="img" aria-label="Photo of a rider in white show clothes standing beside a bay horse in an autumn riding arena"></div>

  <header class="title-band">
    <h1 class="title-script">Essential Oils for</h1>
    <p class="title-sub">The Horse &amp; Rider</p>
  </header>

  <section class="topic left" style="top:164px;height:70px"><h2>BRAIN</h2><p>Grankincense, Mind Spark,<br>Clear Path, Cedarwood</p></section>
  <section class="topic left" style="top:262px;height:70px"><h2>SKIN &amp; HAIR</h2><p>Cedarwood, Lavender,<br>Geranium, Frankincense, Myrrh</p></section>
  <section class="topic left" style="top:360px;height:70px"><h2>EARS</h2><p>Helichrysum, Clean Air,<br>Tea Tree, Juniper</p></section>
  <section class="topic left" style="top:458px;height:70px"><h2>LUNGS</h2><p>B. R., Nightwing, Eucalyptus (all),<br>Guardian, Tea Tree, Golden Tide</p></section>
  <section class="topic left" style="top:554px;height:91px"><h2>MUSCLES</h2><p>AromaCalm, Deep Ease,<br>Marjoram, Cypress<br>Peppermint, Highland Fir</p></section>
  <section class="topic left" style="top:673px;height:91px"><h2>IMMUNE SUPPORT</h2><p>Guardian, Oregano, Clovera,<br>Evergreen, Lemon, Peppermint,<br>Cinnamon Bark, Rosemary</p></section>
  <section class="topic left" style="top:791px;height:70px"><h2>TENDONS &amp; LIGAMENTS</h2><p>Palo Santo, Lemongrass,<br>Rosemary, Peppermint</p></section>
  <section class="topic left" style="top:890px;height:74px"><h2>HOOF (HORSE)</h2><p>Guardian, Tea Tree,<br>Oregano, Frankincense</p></section>

  <section class="topic right" style="top:164px;height:70px;left:501px;width:193px"><h2>EMOTIONAL SUPPORT</h2><p>Steadfast, NOVA, Bright Horizon,<br>Gladden, Lemon</p></section>
  <section class="topic right" style="top:262px;height:70px"><h2>EYES</h2><p>Frankincense, Sandalwood,<br>Carrot Seed, Lemongrass</p></section>
  <section class="topic right" style="top:360px;height:70px"><h2>MOUTH</h2><p>Clove, Clovera, Tea Tree,<br>Wintergreen, Guardian</p></section>
  <section class="topic right" style="top:458px;height:70px"><h2>HEART</h2><p>Orange, Ylang Ylang, Cypress,<br>Helichrysum, Palmarosa</p></section>
  <section class="topic right" style="top:554px;height:70px"><h2>DIGESTION</h2><p>GutWise, TummyRest, Ginger,<br>Fennel, Peppermint</p></section>
  <section class="topic right" style="top:648px;height:70px"><h2>HORMONAL BALANCE</h2><p>Clary Sage, Moonphase,<br>Equilib, Myrtle, Golden Tide</p></section>
  <section class="topic right" style="top:741px;height:70px"><h2>BONES &amp; JOINTS</h2><p>Soothe All, Helichrysum,<br>Wintergreen, Cool Mist, Steadfast</p></section>
  <section class="topic right" style="top:848px;height:69px"><h2>FEET (RIDER)</h2><p>Rooted, Steadfast, Guardian,<br>Clean Air, Oregano</p></section>

  <footer class="disclaimer">Disclaimer : Not evaluated by the FDA, not medical advice.</footer>
</main>
</body>
</html>
```